1 page marketing brochure for subcontractor services for Florida's Petroleum Contamination cleanup

I need a marketing brochure that can be emailed to potential clients to offer our comprehensive service capabilities to Agency Term Contractors in the Coastal Bureau of Habitat Stewardship's (CBHS) Fuel Recovery Initiative. We offer turnkey support from project management, monitoring, reporting, soil and groundwater assessment, remediation system engineering, design, construction, and system rental. We would like to see designs that use the green and goldish colors in our logo. I have attached the icon from our logo and an amateur in-house created design with some key points that are important to us. The icons used as bullet points can change. I've added examples of industry correct drilling icons. I also added a second picture of a system trailer in use. We are open to different Fonts and are open to assistance with copy refinement. This single page flyer is intended only for digital use (email/website) at this time.
Updates

Target Market(s)

Agency Term contractors in Coastal Bureau of Habitat Stewardship Fuel Recovery Initiative

Industry/Entity Type

Petroleum cleanup in Florida

Requirements
Should not have
• Don't show the Brimor name in the photo. See attached examples of industry appropriate drilling icons

```html
<!DOCTYPE html>
<html lang="en">
<head>
<meta charset="utf-8">
<title>Meridian – Subcontracting Partner Flyer</title>
<link rel="stylesheet" href="https://fonts.googleapis.com/css2?family=Lora:wght@400;500&family=Poppins:ital,wght@0,400;0,600;0,700;0,800;1,700;1,800&display=swap">
<style>
:root{
  --green:#126b38;
  --gold:#ad8a00;
  --gold-light:#c9a514;
  --charcoal:#353334;
  --paper:#f9f9f9;
  --stage:#e8e8e8;
  --ink:#2b2b2b;
  --white:#ffffff;
}
*{box-sizing:border-box;margin:0;padding:0}
html,body{width:1200px;height:960px;overflow:hidden;background:var(--stage)}
body{font-family:"Poppins",sans-serif;color:var(--ink)}
.flyer{position:absolute;left:255px;top:33px;width:690px;height:893px;background:var(--paper);overflow:hidden;box-shadow:0 6px 24px rgba(0,0,0,.12)}
.site-photo{position:absolute;left:0;top:0;width:690px;height:470px;
  background:linear-gradient(180deg,#c9ccd2 0%,#b7bcc4 45%,#6d7560 62%,#7a7a78 78%,#8d8c88 100%)}
.brand{position:absolute;left:40px;top:40px;display:flex;align-items:center;gap:14px}
.brand-mark{width:58px;height:58px;background:var(--green)}
.brand-name{font-family:"Lora",serif;font-weight:500;font-size:54px;line-height:1;color:var(--gold)}
.brand-sub{font-family:"Lora",serif;font-weight:500;font-size:14px;line-height:1.25;color:var(--green);margin-top:4px}
.experience-badge{position:absolute;left:60px;top:250px;width:100px;height:100px;border-radius:50%;background:radial-gradient(circle,#e2c04a 0%,#b28f12 60%,#7c620a 100%);border:4px solid #2b2b2b;z-index:2}
.headline-box{position:absolute;left:40px;top:360px;width:330px;height:240px;background:var(--charcoal);border-radius:14px;padding:30px 22px 0 26px}
.headline{font-weight:800;font-size:24px;line-height:1.08;color:var(--white);text-transform:uppercase}
.headline-sub{font-weight:800;font-size:16px;line-height:1.15;color:var(--gold-light);text-transform:uppercase;margin-top:10px}
.headline-tag{font-style:italic;font-weight:700;font-size:13px;color:var(--white);margin-top:12px}
.services{position:absolute;left:395px;top:285px;width:275px;height:325px;background:var(--green);border-radius:16px;overflow:hidden}
.services-title{height:60px;background:var(--gold);color:var(--white);font-weight:800;font-size:20px;text-align:center;line-height:60px;letter-spacing:.5px}
.service-list{list-style:none;padding:14px 14px 0 40px}
.service-list li{height:42px;display:flex;align-items:center;color:var(--white);font-size:14px;line-height:1.15}
.service-icons{position:absolute;left:377px;top:356px;display:flex;flex-direction:column;gap:8px}
.service-icon{width:36px;height:36px;border-radius:50%;background:var(--gold);display:flex;align-items:center;justify-content:center}
.intro{position:absolute;left:40px;top:614px;width:330px}
.intro-title{font-style:italic;font-weight:800;font-size:19px;line-height:1.15;color:var(--gold)}
.intro-text{font-size:9px;line-height:1.35;text-align:justify;margin-top:6px}
.why{position:absolute;left:0;top:795px;width:390px;height:98px;background:var(--green);padding:9px 0 0 40px;color:var(--white)}
.why-title{font-weight:800;font-size:15px;line-height:1.3}
.why-list{list-style:none;margin-top:1px}
.why-list li{font-size:13px;line-height:1.3;display:flex;align-items:center;gap:8px}
.mission{position:absolute;left:390px;top:612px;width:300px;height:281px;background:var(--gold);padding:40px 20px 0 34px;color:var(--white)}
.mission-title{font-weight:800;font-size:15px}
.mission-text{font-style:italic;font-weight:700;font-size:11px;line-height:1.3}
.contact{list-style:none;margin-top:16px}
.contact li{font-size:11.5px;line-height:1.55;display:flex;align-items:center;gap:7px}
</style>
</head>
<body>
<main class="flyer">
  <div class="site-photo" role="img" aria-label="Drilling rig and field technician working at a Brimor fuel station forecourt"></div>

  <header class="brand">
    <div class="brand-mark"></div>
    <div>
      <div class="brand-name">Meridian</div>
      <div class="brand-sub">Field Science and Engineering, Inc.<br>1420 Harbor Pine Rd., Ocala, FL 34470</div>
    </div>
  </header>

  <div class="experience-badge" role="img" aria-label="40 years of experience badge"></div>

  <section class="headline-box">
    <h1 class="headline">Your<br>Subcontracting<br>Partner</h1>
    <p class="headline-sub">For ATCs in Florida's Fuel Recovery Initiative</p>
    <p class="headline-tag">Offering Turnkey Project Support</p>
  </section>

  <section class="services">
    <h2 class="services-title">OUR SERVICES</h2>
    <ul class="service-list">
      <li>Project Management<br>Support</li>
      <li>Soil &amp; Groundwater<br>Assessment</li>
      <li>System Engineering &amp;<br>Design</li>
      <li>Drilling &amp; Well Installation</li>
      <li>System Construction,<br>Rental &amp; O&amp;M</li>
      <li>Monitoring &amp; Reporting</li>
    </ul>
  </section>

  <div class="service-icons" aria-hidden="true">
    <div class="service-icon"><svg width="22" height="22" viewBox="0 0 22 22" fill="none" stroke="#fff" stroke-width="1.6"><path d="M3 14h6v-4h8M13 6v4M10 6h6M3 11v6"/></svg></div>
    <div class="service-icon"><svg width="22" height="22" viewBox="0 0 22 22" fill="none" stroke="#fff" stroke-width="1.6"><path d="M3 16a8 8 0 0 1 16 0z"/><path d="M11 16l4-5"/></svg></div>
    <div class="service-icon"><svg width="22" height="22" viewBox="0 0 22 22" fill="none" stroke="#fff" stroke-width="1.6"><circle cx="11" cy="11" r="4"/><path d="M11 2v4M11 16v4M2 11h4M16 11h4M4.6 4.6l2.8 2.8M14.6 14.6l2.8 2.8M4.6 17.4l2.8-2.8M14.6 7.4l2.8-2.8"/></svg></div>
    <div class="service-icon"><svg width="22" height="22" viewBox="0 0 22 22" fill="none" stroke="#fff" stroke-width="1.6"><path d="M7 3v16M7 3l6 5M5 19h12M7 12h6M10 12v7"/></svg></div>
    <div class="service-icon"><svg width="22" height="22" viewBox="0 0 22 22" fill="none" stroke="#fff" stroke-width="1.6"><rect x="3" y="7" width="16" height="9" rx="4.5"/><path d="M8 7v9"/></svg></div>
    <div class="service-icon"><svg width="22" height="22" viewBox="0 0 22 22" fill="none" stroke="#fff" stroke-width="1.6"><path d="M4 18V12M8 18V9M12 18V13M3 18h16M4 9l4-4 4 3 5-5"/></svg></div>
  </div>

  <section class="intro">
    <h2 class="intro-title">Partner with Experience<br>you can Trust</h2>
    <p class="intro-text">With 40 years of service to CBHS and the Fuel Recovery Initiative, Meridian offers unmatched expertise in all phases of site assessment and remediation.</p>
    <p class="intro-text">For the new contract period, Meridian will not be an ATC and instead will be providing support to ATC firms by subcontracting our services to others. Meridian remains in good standing with CBHS and will continue to offer our high quality comprehensive service capabilities to ATCs across the state.</p>
  </section>

  <section class="mission">
    <h2 class="mission-title">YOUR SUCCESS IS OUR MISSION</h2>
    <p class="mission-text">Together, we restore Florida's environment<br>safely - efficiently - effectively</p>
    <ul class="contact">
      <li><svg width="11" height="11" viewBox="0 0 12 12" fill="none" stroke="#fff" stroke-width="1.2"><path d="M2 1.5l2 0 1 2.5-1.3 1a6 6 0 0 0 2.8 2.8l1-1.3 2.5 1v2a1 1 0 0 1-1 1A9 9 0 0 1 1 2.5a1 1 0 0 1 1-1z"/></svg>555-010-4420</li>
      <li><svg width="11" height="11" viewBox="0 0 12 12" fill="none" stroke="#fff" stroke-width="1.2"><rect x="1" y="2.5" width="10" height="7"/><path d="M1 2.5l5 4 5-4"/></svg>contact@meridianfieldworks.com</li>
      <li><svg width="11" height="11" viewBox="0 0 12 12" fill="none" stroke="#fff" stroke-width="1.2"><circle cx="6" cy="6" r="5"/><path d="M1 6h10M6 1c-2.5 3-2.5 7 0 10M6 1c2.5 3 2.5 7 0 10"/></svg>www.meridianfieldworks.com</li>
    </ul>
  </section>

  <section class="why">
    <h2 class="why-title">WHY CHOOSE MERIDIAN?</h2>
    <ul class="why-list">
      <li><svg width="12" height="12" viewBox="0 0 12 12" fill="none" stroke="#c9a514" stroke-width="2.4"><path d="M1.5 6.5l3 3 6-8"/></svg>Comprehensive Capabilities</li>
      <li><svg width="12" height="12" viewBox="0 0 12 12" fill="none" stroke="#c9a514" stroke-width="2.4"><path d="M1.5 6.5l3 3 6-8"/></svg>Recognized Top Performer</li>
      <li><svg width="12" height="12" viewBox="0 0 12 12" fill="none" stroke="#c9a514" stroke-width="2.4"><path d="M1.5 6.5l3 3 6-8"/></svg>Deep Program Knowledge</li>
      <li><svg width="12" height="12" viewBox="0 0 12 12" fill="none" stroke="#c9a514" stroke-width="2.4"><path d="M1.5 6.5l3 3 6-8"/></svg>Experienced In-house Personnel</li>
    </ul>
  </section>
</main>
</body>
</html>
```